Cover for nonfiction/memoir book "Static Beneath My Skin"

We're looking for a *nonfiction* *memoir* look that is consistent with other covers in that genre.

MUST HAVE:
- It must include the BACK COVER as it will be for print as well as an ebook.
- Title: Static Beneath My Skin
- TITLE MUST BE EASILY READ AT BRINDLECART THUMBNAIL SIZE
- Author name: Dorothea Quell
- At least one of the attached photos of Dorothea
- In COLOR
- The synopsis below
- Space for an endorsement

From the author: "I am looking for a cover that is eye catching and interesting or artistic, rather than just glamorous or pretty. If you like to edit the photos please do not completely remove the wrinkle between my eyebrows as I mention this in the book. It is okay if i look non conventional and my inner Aspie shows a little. The book is a little bit girly, and it would be good for the cover to reflect that, but mildly. No bright pink and purple designs. Please feel free to zoom in or crop the photos as you think works best"

SYNOPSIS (needs to go on the back cover)

Static Beneath My Skin is an acutely honest and often highly entertaining memoir by Dorothea Quell about life with Asperger's Syndrome. The book follows Dorothea in exploring her past and takes the reader with her on her journey to receiving and accepting her diagnosis. Instead of rehashing widely available Asperger's information, Dorothea focuses on discussing the thoughts, feelings and ideas that go along with being an Aspie, giving us a rare peek into what it really feels like to be a person on the spectrum. A must read for all those who enjoy deep personal stories or have a loved one on the spectrum that they wish to understand better.

The book dimensions will be 5x8 trade paperback and 6x9 hardcover (plus 0.25 bleed margin on all sizes - for both sizes).
Here is some more information from the publisher on cover requirements:

"I've attached a sample of both a paperback and hardcover size. Note that the spine width will be different depending on the final length of the book, so it won't be exact. That said, the front and back covers, and the flaps (for the hardcover) will always be the same as shown.
For deliverables, we need the following:

a Creative Suite 6 or earlier native .PSD (Photoshop), .ID (InDesign), or .AI (Illustrator) file. Creative Cloud files cannot be used and will not be accepted.
final file must include layered objects, and cannot be one 'background' image
Final files must be in CMYK color mode, 300dpi minimum
Total Ink saturation must be no more than 240% on any part of the cover. "True" black should use the following CMYK values: 60/40/40/100.
Fonts used in creation of the cover must be either A) embedded or B) sent with the final file
Vector art is preferred for scaling purposes"

Target Market(s)

Women of all ages. People who like psychology and personal stories.
Also parents and family members who may have a loved one on the Autism spectrum.

Requirements
Nice to have
• Bright green new leaves and greenery are good but not necessary.

```html
<!DOCTYPE html>
<html lang="en">
<head>
<meta charset="utf-8">
<title>Static Beneath My Skin — Print Cover</title>
<link href="https://fonts.googleapis.com/css2?family=Amethysta&family=Arimo&family=Noto+Sans:wght@400&display=swap" rel="stylesheet">
<style>
  :root {
    --paper: #ffffff;
    --ink: #111111;
    --spine-rule: #000000;
    --title-green: #4fe03a;
    --title-white: #ffffff;
    --foliage-light: #b7b27a;
    --foliage-mid: #6c6f3a;
    --foliage-dark: #3b4024;
    --grass: #6f7a3c;
    --grass-dark: #4d5528;
    --ground: #8f7f62;
    --ground-dark: #6a5c45;
  }
  * { margin: 0; padding: 0; box-sizing: border-box; }
  html, body { width: 1200px; height: 914px; overflow: hidden; background: var(--paper); }
  .cover {
    position: relative;
    width: 1200px;
    height: 914px;
    background: var(--paper);
    color: var(--ink);
  }

  /* Back cover */
  .back-cover {
    position: absolute;
    left: 0; top: 0;
    width: 552px; height: 914px;
    padding: 84px 30px 0;
    text-align: center;
  }
  .back-title {
    font-family: "Noto Sans", sans-serif;
    font-weight: 400;
    font-size: 43px;
    line-height: 1.1;
    letter-spacing: -0.8px;
    margin-bottom: 10px;
  }
  .synopsis {
    font-family: "Amethysta", serif;
    font-size: 19.2px;
    line-height: 28.2px;
    letter-spacing: -0.2px;
  }
  .endorsement-space {
    height: 300px;
  }

  /* Spine */
  .spine-rule {
    position: absolute;
    left: 552px; top: 0;
    width: 4px; height: 914px;
    background: var(--spine-rule);
  }
  .spine {
    position: absolute;
    left: 556px; top: 0;
    width: 61px; height: 914px;
    font-family: "Arimo", sans-serif;
    color: var(--ink);
  }
  .spine-title, .spine-author {
    position: absolute;
    left: 50%;
    white-space: nowrap;
    line-height: 1;
    transform-origin: left top;
    transform: rotate(90deg) translateY(-50%);
  }
  .spine-title { top: 131px; font-size: 29px; }
  .spine-author { top: 685px; font-size: 22px; }

  /* Front cover */
  .front-cover {
    position: absolute;
    left: 617px; top: 0;
    width: 583px; height: 914px;
    overflow: hidden;
  }
  .front-photo {
    position: absolute;
    inset: 0;
    background:
      radial-gradient(ellipse 45% 22% at 60% 52%, rgba(140,150,170,0.55) 0%, rgba(140,150,170,0) 100%),
      radial-gradient(ellipse 30% 18% at 80% 12%, rgba(200,195,140,0.6) 0%, rgba(200,195,140,0) 100%),
      radial-gradient(ellipse 25% 20% at 15% 25%, rgba(170,165,110,0.45) 0%, rgba(170,165,110,0) 100%),
      linear-gradient(180deg,
        var(--foliage-dark) 0%,
        var(--foliage-mid) 20%,
        var(--foliage-dark) 36%,
        var(--grass) 48%,
        var(--grass-dark) 66%,
        var(--ground) 80%,
        var(--ground-dark) 100%);
  }
  .front-title {
    position: absolute;
    left: 0; right: 0; top: 30px;
    text-align: center;
    font-family: "Noto Sans", sans-serif;
    font-weight: 400;
    line-height: 1;
  }
  .front-title .title-lead {
    display: block;
    color: var(--title-green);
    font-size: 124px;
    letter-spacing: -3px;
  }
  .front-title .title-rest {
    display: block;
    color: var(--title-white);
    font-size: 72px;
    letter-spacing: -2.5px;
    margin-top: 0;
  }
  .front-author {
    position: absolute;
    left: 0; right: 0; top: 822px;
    text-align: center;
    font-family: "Arimo", sans-serif;
    font-size: 60px;
    color: var(--title-white);
    line-height: 1;
  }
</style>
</head>
<body>
  <main class="cover">
    <section class="back-cover">
      <h2 class="back-title">Static Beneath My Skin</h2>
      <p class="synopsis">Static Beneath My Skin is an acutely honest and often highly entertaining memoir by Dorothea Quell about life with Asperger's Syndrome. The book follows Dorothea in exploring her past and takes the reader with her on her journey to receiving and accepting her diagnosis. Instead of rehashing widely available Asperger's information, Dorothea focuses on discussing the thoughts, feelings and ideas that go along with being an Aspie, giving us a rare peek into what it really feels like to be a person on the spectrum. A must read for all those who enjoy deep personal stories or have a loved one on the spectrum that they wish to understand better.</p>
      <div class="endorsement-space" aria-label="Reserved space for an endorsement"></div>
    </section>

    <div class="spine-rule"></div>

    <section class="spine">
      <span class="spine-title">Static Beneath My Skin</span>
      <span class="spine-author">Dorothea Quell</span>
    </section>

    <section class="front-cover">
      <div class="front-photo" role="img" aria-label="Photograph of the author in a blue dress lying on her stomach in grass, holding a small yellow flower, sunlit foliage behind and a dusty path in front"></div>
      <h1 class="front-title">
        <span class="title-lead">Static</span>
        <span class="title-rest">Beneath My Skin</span>
      </h1>
      <p class="front-author">Dorothea Quell</p>
    </section>
  </main>
</body>
</html>
```